Flyer for annual KESTREL SUMMIT 2020

I would like a church event flyer designed. The event is called "KESTREL SUMMIT 2020". I am looking for a professional, yet catchy design that uses our brand colors and logo creatively while communicating key information of the event effectively.

1. The logo is attached in two color formats. The designer has the choice to use them as he/she want.

2. The location of the event is: Harlow Community Center, 239 Fennimore Street, Portland, ME 04117

3. Time and date of event. The designer can organize and format the date and time as he/she pleases.
Thursday December 31st @ 6:30PM
Friday January 1st @ 6:30PM
Saturday 2nd @ 6:30PM
Sunday 3rd @ 4:30PM

4. The topic of the event is "In Fire and On Fire". The designer is free to use this phrase as he/she pleases to create a good composition.

5. Speaker: Prophet Marcus Olunde (2 pictures of the speaker to choose from are attached)

6. Contact information: contact@brightmeadowfold.org - Telephone number: 207 583 2914

7. I would also like the following three words on the flyer. These words describe the focus of the event: FIRE, REVIVAL, PROPHETIC

Target Market(s)

Young adults

Font styles to use
Sans Serif

Requirements
Must have
• Logo, speaker's picture
Should not have
• cross image, church image

```html
<!DOCTYPE html>
<html lang="en">
<head>
<meta charset="utf-8">
<title>Kestrel Summit 2020 Flyer</title>
<link rel="stylesheet" href="https://fonts.googleapis.com/css2?family=Poppins:wght@700;800&family=Roboto:wght@400;500;700&family=Roboto+Slab:wght@700&display=swap">
<style>
  :root {
    --navy: #0f3a5c;
    --navy-deep: #0b2f4c;
    --orange: #f7931e;
    --orange-deep: #e0681a;
    --flame: #ffb12e;
    --white: #ffffff;
    --stage: #ebebeb;
    --ember: #5a0f0a;
    --rule: rgba(255,255,255,0.35);
  }
  * { margin: 0; padding: 0; box-sizing: border-box; }
  html, body { width: 672px; height: 1200px; overflow: hidden; }
  body { background: var(--stage); position: relative; font-family: "Roboto", Arial, sans-serif; }

  .flyer {
    position: absolute; left: 36px; top: 176px; width: 600px; height: 849px;
    background: linear-gradient(180deg, var(--navy) 0%, var(--navy-deep) 100%);
    overflow: hidden; box-shadow: 0 6px 22px rgba(0,0,0,0.28); color: var(--white);
  }
  .flyer-art { position: absolute; inset: 0; }

  .brand {
    position: absolute; left: 56px; top: 70px; display: flex; align-items: center; gap: 10px;
    font-family: "Poppins", Arial, sans-serif; font-weight: 700; font-size: 40px; letter-spacing: 2px; color: var(--white);
  }
  .brand-dot { width: 18px; height: 18px; border-radius: 50%; background: var(--orange); }

  .title { position: absolute; left: 54px; top: 160px; font-family: "Poppins", Arial, sans-serif; font-weight: 800; line-height: 1; }
  .title-main { display: block; font-size: 50px; color: var(--white); letter-spacing: -0.5px; }
  .title-sub { display: block; font-size: 33px; color: var(--orange); margin-top: 8px; letter-spacing: 0.5px; }
  .title-year { display: block; font-size: 94px; color: var(--white); margin-top: 4px; letter-spacing: -3px; }

  .info { position: absolute; left: 56px; width: 215px; font-size: 10.5px; line-height: 1.35; }
  .info-location { top: 393px; padding-left: 18px; }
  .info-location strong { font-weight: 700; }
  .info-note { top: 466px; }
  .info-dates { top: 524px; padding-left: 20px; }
  .info-dates .day { color: var(--orange); font-weight: 500; }
  .rule { position: absolute; left: 56px; width: 210px; height: 1px; background: var(--rule); }
  .rule-one { top: 454px; }
  .rule-two { top: 513px; }
  .info-icon { position: absolute; left: 0; top: 1px; }

  .theme-badge {
    position: absolute; left: 54px; top: 604px; width: 232px; height: 120px;
    border-radius: 14px;
    background: radial-gradient(ellipse at center, #ffd27a 0%, #f39a24 45%, rgba(232,110,20,0.0) 75%);
  }
  .theme-plate {
    position: absolute; left: 18px; top: 26px; width: 196px; height: 68px;
    background: linear-gradient(180deg, #7a1a10 0%, var(--ember) 100%);
    border: 3px solid #f6c14b; border-radius: 4px;
    display: flex; flex-direction: column; align-items: center; justify-content: center;
    font-family: "Roboto Slab", Georgia, serif; font-weight: 700; font-size: 22px; line-height: 1.05; color: var(--flame); text-align: center;
  }

  .speaker {
    position: absolute; left: 291px; top: 664px; width: 309px; height: 68px;
    background: var(--orange); padding: 14px 0 0 24px; font-family: "Poppins", Arial, sans-serif;
  }
  .speaker-label { display: block; font-size: 11px; font-weight: 700; color: var(--navy); line-height: 1; }
  .speaker-name { display: block; font-size: 21px; font-weight: 800; color: var(--white); line-height: 1.2; }

  .focus {
    position: absolute; left: 48px; top: 752px; display: flex; gap: 22px;
    font-family: "Poppins", Arial, sans-serif; font-weight: 800; font-size: 23px; line-height: 1;
  }
  .focus-item { display: flex; align-items: center; gap: 7px; }

  .contact {
    position: absolute; left: 52px; top: 802px; display: flex; gap: 12px; font-size: 14.5px; letter-spacing: 0.2px;
  }
  .contact-item { display: flex; align-items: center; gap: 7px; }
</style>
</head>
<body>
  <main class="flyer">
    <svg class="flyer-art" width="600" height="849" viewBox="0 0 600 849">
      <defs>
        <radialGradient id="fireGlow" cx="0.5" cy="0.5" r="0.5">
          <stop offset="0" stop-color="#ffd35a"/>
          <stop offset="0.55" stop-color="#f7931e"/>
          <stop offset="1" stop-color="#d9541a"/>
        </radialGradient>
        <linearGradient id="speakerTone" x1="0" y1="0" x2="0" y2="1">
          <stop offset="0" stop-color="#c9481f"/>
          <stop offset="0.6" stop-color="#d85a26"/>
          <stop offset="1" stop-color="#243e72"/>
        </linearGradient>
      </defs>
      <path class="accent-white" d="M440 0 H600 V300 C520 230 440 150 440 0 Z" fill="var(--white)"/>
      <path class="accent-orange" d="M420 0 C400 60 430 150 520 200 C560 225 590 250 600 270 V330 C540 290 470 250 440 190 C405 130 400 60 420 0 Z" fill="var(--orange)"/>
      <path class="accent-orange-ring" d="M600 120 C560 150 560 200 600 240 Z" fill="var(--orange)"/>
      <path class="fire-disc" d="M320 420 C250 460 240 580 320 640 L360 640 L360 410 Z" fill="url(#fireGlow)" stroke="var(--white)" stroke-width="5"/>
      <g role="img" aria-label="Photo of the speaker, seated, wearing an orange jacket and navy trousers">
        <path d="M345 90 C380 70 440 70 470 100 C490 130 520 160 560 190 C590 215 600 250 600 300 V664 H300 C300 600 320 560 340 520 C350 460 345 300 345 90 Z" fill="url(#speakerTone)"/>
      </g>
    </svg>

    <div class="brand"><span class="brand-dot"></span>CORVANE</div>

    <h1 class="title">
      <span class="title-main">KESTREL</span>
      <span class="title-sub">SUMMIT</span>
      <span class="title-year">2020</span>
    </h1>

    <p class="info info-location">
      <svg class="info-icon" width="12" height="14" viewBox="0 0 12 14"><path d="M6 0 C2.7 0 0 2.6 0 5.8 C0 9.5 6 14 6 14 C6 14 12 9.5 12 5.8 C12 2.6 9.3 0 6 0 Z" fill="var(--orange)"/><circle cx="6" cy="5.6" r="2.2" fill="var(--navy)"/></svg>
      The location of the event is:<br>
      <strong>Harlow Community Center, 239 Fennimore Street, Portland, ME 04117</strong>
    </p>
    <div class="rule rule-one"></div>
    <p class="info info-note">Time and date of event. The designer can organize and format the date and time as he/she pleases</p>
    <div class="rule rule-two"></div>
    <p class="info info-dates">
      <svg class="info-icon" width="13" height="13" viewBox="0 0 13 13"><rect x="0.75" y="1.75" width="11.5" height="10.5" rx="1.5" fill="none" stroke="var(--orange)" stroke-width="1.2"/><line x1="0.75" y1="4.8" x2="12.25" y2="4.8" stroke="var(--orange)" stroke-width="1.2"/></svg>
      <span class="day">Thursday December</span> 31st @ 6:30PM<br>
      <span class="day">Friday January</span> 1st @ 6:30PM<br>
      <span class="day">Saturday</span> 2nd @ 6:30PM<br>
      <span class="day">Sunday</span> 3rd @ 4:30PM
    </p>

    <div class="theme-badge">
      <div class="theme-plate"><span>IN FIRE AND</span><span>ON FIRE</span></div>
    </div>

    <div class="speaker">
      <span class="speaker-label">SPEAKER:</span>
      <span class="speaker-name">Prophet Marcus Olunde</span>
    </div>

    <div class="focus">
      <span class="focus-item">
        <svg width="18" height="26" viewBox="0 0 18 26"><path d="M9 0 C11 6 18 9 18 17 C18 22 14 26 9 26 C4 26 0 22 0 17 C0 12 4 10 5 5 C7 8 7 11 9 12 C10 8 9 4 9 0 Z" fill="var(--orange)"/></svg>FIRE</span>
      <span class="focus-item">
        <svg width="26" height="24" viewBox="0 0 26 24"><path d="M13 4 L17 10 L23 6 L21 20 H5 L3 6 L9 10 Z" fill="none" stroke="var(--orange)" stroke-width="2.2" stroke-linejoin="round"/></svg>REVIVAL</span>
      <span class="focus-item">
        <svg width="22" height="26" viewBox="0 0 22 26"><circle cx="11" cy="7" r="5.5" fill="none" stroke="var(--orange)" stroke-width="2.2"/><path d="M2 25 C2 18 6 14 11 14 C16 14 20 18 20 25 Z" fill="var(--orange)"/></svg>PROPHETIC</span>
    </div>

    <div class="contact">
      <span class="contact-item">
        <svg width="15" height="15" viewBox="0 0 15 15"><path d="M3 1 L5.5 1 L6.5 4.5 L4.8 5.8 C5.6 7.6 7.4 9.4 9.2 10.2 L10.5 8.5 L14 9.5 L14 12 C14 13 13 14 12 14 C6 14 1 9 1 3 C1 2 2 1 3 1 Z" fill="none" stroke="var(--orange)" stroke-width="1.5"/></svg>
        Telephone number: 207 583 2914</span>
      <span class="contact-item">
        <svg width="14" height="14" viewBox="0 0 14 14"><rect x="1" y="3" width="12" height="9" rx="1" fill="none" stroke="var(--orange)" stroke-width="1.5"/><path d="M1 3.5 L7 8 L13 3.5" fill="none" stroke="var(--orange)" stroke-width="1.5"/></svg>
        contact@brightmeadowfold.org</span>
    </div>
  </main>
</body>
</html>
```